New Start Up Website for Volt Ranger Mobile - Mobile EV Charging

I need an informational website built to support my new start up. Should be clean and very straight forward. Home, About, Vehicles we Support, Links to iOS and Android apps, Contact Us. Volt Ranger Mobile is an emergency / express EV charging solution. Charging as a Service as the industry is being dubbed. I believe I am second to market next to Brisk Amp and their Surgely mobile solution.
Updates

Website must be built on Wordpress!

Target Market(s)

EV Owners

Industry/Entity Type

EV Charging

Coding

Coded - Design and coding required

Number of Pages Required

4 page

Font styles to use
Sans Serif

Colors
59FF00
82FF00
B8FF75
E3FFCB
F4FFEA

Requirements
Must have
• I will not have any real pics for at least 60 days. I will need place holders or a mock up of the vehicle.
Nice to have
• Briskamp.io is our competitor. They own Surgely APP which is what we're modeling.

```html
<!DOCTYPE html>
<html lang="en">
<head>
<meta charset="utf-8">
<title>Volt Ranger Mobile – Express EV Charging</title>
<link href="https://fonts.googleapis.com/css2?family=Exo+2:ital,wght@1,700;1,800&family=Roboto:wght@400;500;700&display=swap" rel="stylesheet">
<style>
:root{
  --blue:#1d3fe0;
  --blue-dark:#0f2a9e;
  --navy:#17204a;
  --green:#2fc51f;
  --green-bright:#59ff00;
  --ink:#1c1f2a;
  --muted:#5a5f6e;
  --grey-bg:#eef0f4;
  --white:#ffffff;
}
*{box-sizing:border-box;margin:0;padding:0}
html,body{width:1200px;height:4093px;overflow:hidden}
body{position:relative;font-family:"Roboto",sans-serif;color:var(--ink);background:var(--white)}
.abs{position:absolute}
.heading{font-family:"Exo 2",sans-serif;font-style:italic;font-weight:800;text-transform:uppercase;line-height:1.05;color:var(--navy)}
.eyebrow{font-size:16px;letter-spacing:1.5px;text-transform:uppercase;color:var(--blue);display:flex;align-items:center;gap:12px}
.eyebrow::after{content:"";width:105px;height:2px;background:var(--green)}
.copy{font-size:14px;line-height:27px;color:var(--muted)}
.btn{display:inline-flex;align-items:center;justify-content:center;border-radius:24px;font-size:13px;font-weight:700;color:#fff;text-transform:uppercase;letter-spacing:.3px}
.btn-green{background:var(--green)}
.btn-blue{background:var(--blue)}
.photo{position:absolute}

/* header */
.site-header{top:0;left:0;width:1200px;height:80px;background:#fff}
.brand{display:flex;align-items:center;gap:10px}
.brand-dot{width:28px;height:28px;border-radius:50%;background:var(--blue)}
.brand-name{font-weight:700;font-size:20px;color:var(--blue);text-transform:uppercase;letter-spacing:.3px}
.nav{top:0;left:528px;height:80px;display:flex;align-items:center;gap:50px;font-size:14px;color:#3a3f4d}
.nav .active{font-weight:700;color:var(--ink)}

/* hero */
.hero{top:80px;left:0;width:1200px;height:633px;overflow:hidden;background:#1f2124}
.hero-photo{right:0;top:0;width:760px;height:633px;background:linear-gradient(120deg,#3a4150 0%,#8b929c 35%,#e6e8eb 65%,#ffffff 100%)}
.hero-text{left:112px;top:190px;color:#fff}
.hero-text .kicker{font-size:22px;letter-spacing:2px;display:flex;align-items:center;gap:10px}
.hero-text .kicker::after{content:"";width:110px;height:2px;background:var(--green)}
.hero-text h1{font-family:"Exo 2",sans-serif;font-style:italic;font-weight:800;text-transform:uppercase;line-height:1.08;margin-top:14px}
.hero-text h1 .l1{font-size:52px;font-weight:700}
.hero-text h1 .l2{font-size:56px;display:block}
.hero-text p{font-size:14px;line-height:23px;width:440px;margin-top:18px}
.down{left:568px;top:681px;width:64px;height:64px;border-radius:50%;background:#fff;box-shadow:0 4px 16px rgba(0,0,0,.12);display:flex;align-items:center;justify-content:center}

/* about */
.about-photo-a{left:78px;top:800px;width:390px;height:262px;clip-path:polygon(18% 0,100% 0,82% 100%,0 100%);background:linear-gradient(135deg,#cfe0ef,#3f7fc4 60%,#1d3f8a)}
.about-photo-b{left:300px;top:1014px;width:306px;height:242px;clip-path:polygon(18% 0,100% 0,82% 100%,0 100%);background:linear-gradient(135deg,#e7e2dc,#6a5550 55%,#221a1c)}

/* solution */
.solution{top:1340px;left:0;width:1200px;height:570px;overflow:hidden;background:linear-gradient(120deg,#1c3fd6,#0d2a9a)}
.solution-photo{left:430px;top:0;width:770px;height:570px;clip-path:polygon(28% 0,100% 0,100% 100%,0 100%);background:linear-gradient(135deg,#7c8fa8,#2d3b55 55%,#121a2c)}
.solution-text{left:125px;top:112px;color:#fff}
.solution-text .eyebrow{color:#fff}
.solution-text .eyebrow::after{background:#4a7bff}
.solution-text .heading{color:#fff;font-size:40px;margin-top:12px}
.solution-text p{font-size:14px;line-height:27px;width:370px;margin-top:16px}

/* vehicles */
.vehicle{top:2108px;height:326px;overflow:hidden}
.vehicle-label{position:absolute;left:0;right:0;bottom:26px;text-align:center;color:#fff;font-weight:700;font-size:19px;text-transform:uppercase}
.vehicle-label::after{content:"";display:block;width:44px;height:2px;background:var(--green);margin:6px auto 0}
.vehicle-featured{left:296px;top:2078px;width:298px;height:383px;background:linear-gradient(180deg,#2a3a7a,#19285f);text-align:center;color:#fff;padding:100px 22px 0}
.vehicle-featured h3{font-size:22px;font-weight:500;text-transform:uppercase}
.vehicle-featured p{font-size:13px;line-height:20px;margin-top:14px}

/* app */
.app-media{left:125px;top:2533px;width:438px;height:452px;border-radius:70px 0 70px 0;background:linear-gradient(135deg,#4fd840 0%,#22b62a 55%,#0e9a1e 100%)}
.store{top:2830px;width:170px;height:52px;border-radius:6px;background:#111;color:#fff;display:flex;align-items:center;gap:12px;padding:0 14px}
.store-mark{width:26px;height:26px;border-radius:50%;background:#fff}
.store small{display:block;font-size:10px}
.store b{display:block;font-size:19px;font-weight:500;line-height:1}

/* blogs */
.blogs{top:3075px;left:0;width:1200px;height:635px;background:var(--grey-bg)}
.post-img{top:3238px;width:318px;height:212px}
.post{top:3420px;width:293px;height:200px;background:#fff;padding:18px 24px}
.post-date{font-size:12px;font-weight:700;color:var(--blue);display:flex;align-items:center;gap:5px}
.post h4{font-size:14px;font-weight:700;line-height:22px;margin-top:10px;text-transform:uppercase}
.post p{font-size:11px;line-height:19px;color:var(--muted);margin-top:8px}
.post .btn{height:30px;width:118px;font-size:10px;margin-top:14px;border-radius:16px}

/* footer */
.footer-col{top:3710px;height:260px;border-left:1px solid #e1e3e8;padding:70px 0 0 22px}
.footer-col h5{font-size:17px;font-weight:700;color:var(--blue);text-transform:uppercase;border-left:3px solid var(--green);padding-left:10px;margin-left:-22px}
.footer-col ul{list-style:none;margin-top:14px}
.footer-col li{font-size:12px;color:#444;line-height:28px}
.contact-row{display:flex;align-items:flex-start;gap:12px;font-size:12px;line-height:18px;color:#444;margin-top:14px}
.contact-ico{width:24px;height:24px;border-radius:50%;background:var(--blue);flex:none;display:flex;align-items:center;justify-content:center}
.social{width:26px;height:26px;border-radius:50%;background:#222}
.copyright{top:4036px;left:0;width:1200px;height:57px;background:#f0f1f4;display:flex;align-items:center;justify-content:center;font-size:12px;color:#444}
</style>
</head>
<body>

<header class="site-header abs">
  <div class="brand abs" style="left:113px;top:26px">
    <span class="brand-dot"></span><span class="brand-name">Volt Ranger Mobile</span>
  </div>
  <nav class="nav abs">
    <span class="active">ABOUT</span><span>VEHICLES WE SUPPORT</span><span>MOBILE APP</span><span>CONTACT US</span>
  </nav>
</header>

<section class="hero abs">
  <div class="photo hero-photo" role="img" aria-label="Close-up of an EV charging plug connected to a white car"></div>
  <svg class="abs" style="left:0;top:0" width="1200" height="633" viewBox="0 0 1200 633">
    <polygon points="420,0 520,0 430,220 635,220 300,633 250,633 350,330 290,330" fill="#1b3ef0" opacity=".95"/>
  </svg>
  <div class="hero-text abs">
    <div class="kicker">VOLT RANGER MOBILE</div>
    <h1><span class="l1">100% Express</span><span class="l2">EV Charging</span></h1>
    <p>We offer a suite of products and solutions that make managing all aspects of EV charging seamless, simple and convenient.</p>
    <a class="btn btn-green" style="width:170px;height:44px;margin-top:26px">Learn More</a>
  </div>
</section>
<div class="down abs">
  <svg width="26" height="26" viewBox="0 0 24 24" fill="none" stroke="#2fc51f" stroke-width="2"><path d="M12 4v15M6 13l6 6 6-6"/></svg>
</div>

<section class="about">
  <div class="photo about-photo-a" role="img" aria-label="Driver plugging a charger into a blue car while holding a phone"></div>
  <div class="photo about-photo-b" role="img" aria-label="Hand holding a phone with a charging app beside a car"></div>
  <svg class="abs" style="left:160px;top:900px" width="380" height="290" viewBox="0 0 380 290">
    <polyline points="290,10 370,10 362,100" fill="none" stroke="#2fc51f" stroke-width="3"/>
    <polyline points="30,205 15,285 150,285" fill="none" stroke="#2fc51f" stroke-width="3"/>
    <polygon points="358,50 345,78 354,78 346,100 362,68 353,68" fill="#1d3fe0"/>
  </svg>
  <div class="abs" style="left:658px;top:852px">
    <div class="eyebrow">Who We Are</div>
    <h2 class="heading" style="font-size:38px;margin-top:10px">About Volt Ranger<br>Mobile</h2>
    <p class="copy" style="width:455px;margin-top:22px">Lorem Ipsum is simply dummy text of the printing and typesetting industry. Lorem Ipsum has been the industry's standard dummy text ever since the 1500s, when an unknown printer took a galley of type and scrambled it to make a type specimen book. It has survived not only five centuries, but also the leap into electronic typesetting, remaining essentially unchanged.</p>
    <a class="btn btn-green" style="width:170px;height:44px;margin-top:28px">Learn More</a>
  </div>
</section>

<section class="solution abs">
  <div class="photo solution-photo" role="img" aria-label="White electric car charging at a wall-mounted station in a garage"></div>
  <svg class="abs" style="left:0;top:0" width="1200" height="570" viewBox="0 0 1200 570">
    <line x1="660" y1="0" x2="400" y2="570" stroke="#2fc51f" stroke-width="5"/>
  </svg>
  <div class="solution-text abs">
    <div class="eyebrow">What We Do</div>
    <h2 class="heading">EV Charging<br>Solution</h2>
    <p>Lorem Ipsum is simply dummy text of the printing and typesetting industry. Lorem Ipsum has been the industry's standard dummy text ever since the 1500s, when an unknown printer took a galley of type and scrambled it to make a type specimen book.</p>
    <a class="btn btn-green" style="width:170px;height:42px;margin-top:18px">Download App</a>
  </div>
</section>

<section class="vehicles">
  <div class="abs" style="left:0;top:1968px;width:1200px;text-align:center">
    <div class="eyebrow" style="justify-content:center"><span style="width:52px;height:2px;background:var(--green)"></span>Echarging Vehicles</div>
    <h2 class="heading" style="font-size:34px;margin-top:10px">Vehicles We Support</h2>
  </div>
  <div class="photo vehicle" style="left:0;width:291px;background:linear-gradient(180deg,#8a8f94,#5f6b5a 70%,#3d4a34)" role="img" aria-label="Silver SUV parked on a street">
    <div class="vehicle-label">Vehicle Lorem</div>
  </div>
  <div class="vehicle-featured abs" role="img" aria-label="Dark blue car photo behind featured vehicle text">
    <h3>Vehicle Lorem</h3>
    <p>Lorem Ipsum is simply dummy text of the printing and typesetting industry, Lorem Ipsum has been the industry's standard dummy</p>
    <a class="btn btn-blue" style="width:154px;height:38px;margin-top:20px">Learn More</a>
  </div>
  <div class="photo vehicle" style="left:598px;width:299px;background:linear-gradient(180deg,#9aa3ad,#5c6670 60%,#2f363e)" role="img" aria-label="White car connected to a charging cable">
    <div class="vehicle-label">Vehicle Lorem</div>
  </div>
  <div class="photo vehicle" style="left:901px;width:299px;background:linear-gradient(180deg,#b9b4ad,#7b7a78 60%,#3c3b3a)" role="img" aria-label="Compact electric hatchback at a city charging spot">
    <div class="vehicle-label">Vehicle Lorem</div>
  </div>
</section>

<section class="app">
  <div class="photo app-media" role="img" aria-label="Hand holding a phone that shows the charging app, over a green backdrop"></div>
  <div class="abs" style="left:640px;top:2622px">
    <div class="eyebrow">Get Started Now</div>
    <h2 class="heading" style="font-size:36px;margin-top:10px">Download Our<br>Echarging Mobile App</h2>
    <p class="copy" style="width:470px;margin-top:18px">Lorem Ipsum is simply dummy text of the printing and typesetting industry. Lorem Ipsum has been the industry's standard</p>
  </div>
  <div class="store abs" style="left:640px"><span class="store-mark"></span><span><small>GET IT ON</small><b>Play Shelf</b></span></div>
  <div class="store abs" style="left:823px"><span class="store-mark"></span><span><small>Download on</small><b>App Depot</b></span></div>
</section>

<section class="blogs abs">
  <div style="text-align:center;margin-top:68px">
    <div style="font-size:15px;letter-spacing:1.5px;color:var(--blue)">RECENT POSTS</div>
    <h2 class="heading" style="font-size:34px;margin-top:8px">Our Latest Blogs</h2>
  </div>
</section>
<div class="photo post-img" style="left:100px;background:linear-gradient(160deg,#e9e2c8,#9aa29a 60%,#5c605c)" role="img" aria-label="Two people standing beside a white car"></div>
<div class="photo post-img" style="left:446px;background:linear-gradient(160deg,#d7e4ee,#7fa6c8 55%,#3b5d80)" role="img" aria-label="Charging plug inserted into a car port"></div>
<div class="photo post-img" style="left:792px;background:linear-gradient(160deg,#dfe3e8,#8aa0b8 55%,#34465e)" role="img" aria-label="Hand holding a phone with charging app"></div>

<article class="post abs" style="left:112px">
  <div class="post-date"><svg width="12" height="12" viewBox="0 0 12 12" fill="none" stroke="#2fc51f"><rect x="1" y="2" width="10" height="9"/><path d="M1 5h10M4 1v2M8 1v2"/></svg>25 SEP 2022</div>
  <h4>Lorem ipsum dolor sit amet, consect etur adipi</h4>
  <p>Sed ut perspiciatis unde omnis iste natus error sit voluptatem accusantium doloremque</p>
  <a class="btn btn-blue">Learn More</a>
</article>
<article class="post abs" style="left:459px">
  <div class="post-date"><svg width="12" height="12" viewBox="0 0 12 12" fill="none" stroke="#2fc51f"><rect x="1" y="2" width="10" height="9"/><path d="M1 5h10M4 1v2M8 1v2"/></svg>25 SEP 2022</div>
  <h4>Lorem ipsum dolor sit amet, consect etur adipi</h4>
  <p>Sed ut perspiciatis unde omnis iste natus error sit voluptatem accusantium doloremque</p>
  <a class="btn btn-blue">Learn More</a>
</article>
<article class="post abs" style="left:806px">
  <div class="post-date"><svg width="12" height="12" viewBox="0 0 12 12" fill="none" stroke="#2fc51f"><rect x="1" y="2" width="10" height="9"/><path d="M1 5h10M4 1v2M8 1v2"/></svg>25 SEP 2022</div>
  <h4>Lorem ipsum dolor sit amet, consect etur adipi</h4>
  <p>Sed ut perspiciatis unde omnis iste natus error sit voluptatem accusantium doloremque</p>
  <a class="btn btn-blue">Learn More</a>
</article>

<footer>
  <div class="brand abs" style="left:112px;top:3826px">
    <span class="brand-dot"></span><span class="brand-name" style="font-size:21px">Volt Ranger Mobile</span>
  </div>
  <div class="abs" style="left:200px;top:3898px;display:flex;gap:6px">
    <span class="social"></span><span class="social"></span><span class="social"></span><span class="social"></span>
  </div>
  <div class="footer-col abs" style="left:455px;width:215px">
    <h5>Navigation</h5>
    <ul><li>About Us</li><li>Vehicles we support</li><li>Download Our App</li><li>Contact Us</li></ul>
  </div>
  <div class="footer-col abs" style="left:670px;width:178px">
    <h5>Resources</h5>
    <ul><li>Support</li><li>Terms of Use</li><li>Privacy Policy</li><li>FAQ</li></ul>
  </div>
  <div class="footer-col abs" style="left:848px;width:352px">
    <h5>Contact Us</h5>
    <div class="contact-row" style="margin-top:18px"><span class="contact-ico"><svg width="12" height="12" viewBox="0 0 24 24" fill="#fff"><path d="M12 2a7 7 0 0 0-7 7c0 5 7 13 7 13s7-8 7-13a7 7 0 0 0-7-7zm0 9.5a2.5 2.5 0 1 1 0-5 2.5 2.5 0 0 1 0 5z"/></svg></span><span>418 Harbor Lane<br>Maplewood, City 12345</span></div>
    <div class="contact-row" style="margin-top:20px"><span class="contact-ico"><svg width="12" height="12" viewBox="0 0 24 24" fill="#fff"><path d="M6.6 10.8a15 15 0 0 0 6.6 6.6l2.2-2.2c.3-.3.7-.4 1-.2 1.1.4 2.3.6 3.6.6.6 0 1 .4 1 1V20c0 .6-.4 1-1 1A17 17 0 0 1 3 4c0-.6.4-1 1-1h3.5c.6 0 1 .4 1 1 0 1.3.2 2.5.6 3.6.1.3 0 .7-.2 1z"/></svg></span><span style="line-height:24px">(555) 014 2278</span></div>
    <div class="contact-row" style="margin-top:20px"><span class="contact-ico"><svg width="12" height="12" viewBox="0 0 24 24" fill="#fff"><path d="M3 5h18v14H3zm2 2v.5l7 4.5 7-4.5V7z"/></svg></span><span style="line-height:24px">hello@voltranger.io</span></div>
  </div>
  <div class="copyright abs">© 2022&nbsp;<u>Volt Ranger Mobile.</u>&nbsp;All Right Reserved</div>
</footer>

</body>
</html>
```